Criação de Power Point Slide Mestre para Consultoria de Negócios
" Com os meus conhecimentos profissionais (acadêmicos e por experiência), procuro identificar no mercado em quais empresas posso oferecer os meus serviços. Procuro passar a imagem de que a consultoria é algo que não "algema" a empresa e tampouco a pune por erros já cometidos. Procuro sempre deixar claro que a consultoria não executa as ações, ela conversa com a gestão e essa sim é que decide se a proposta da consultoria vai ao encontro dos objetivos dos proprietários. Costumo ressaltar que a consultoria é a teoria a serviço da pratica na gestão. Gestão e Controles são palavras de ordem. "

```html
<!DOCTYPE html>
<html lang="pt-BR">
<head>
<meta charset="utf-8">
<title>Slide mestre – Nórdica Consultoria</title>
<link rel="stylesheet" href="https://fonts.googleapis.com/css2?family=Libre+Baskerville&family=Roboto+Condensed:ital,wght@1,700&display=swap">
<style>
  :root {
    --canvas: #f4f4f5;
    --slide-light: #f7f7f8;
    --slide-mid: #e6e8ec;
    --navy: #1c3566;
    --navy-deep: #0f2450;
    --blue: #1f4fa0;
    --blue-light: #5b8fd6;
    --photo-light: #d9dde3;
    --photo-dark: #3c4658;
    --white: #ffffff;
  }
  html, body {
    margin: 0;
    width: 1200px;
    height: 1200px;
    overflow: hidden;
    background: var(--canvas);
  }
  .slide {
    position: absolute;
    left: 0;
    top: 225px;
    width: 1200px;
    height: 750px;
    overflow: hidden;
    background: linear-gradient(135deg, var(--slide-light) 0%, var(--slide-mid) 100%);
  }
  .slide-art {
    position: absolute;
    inset: 0;
  }
  .brand {
    position: absolute;
    left: 150px;
    top: 300px;
    display: flex;
    align-items: center;
    gap: 22px;
  }
  .brand-square {
    width: 70px;
    height: 70px;
    background: var(--navy);
  }
  .brand-name {
    font-family: "Libre Baskerville", serif;
    font-size: 46px;
    line-height: 1.15;
    color: var(--navy);
    letter-spacing: 0.5px;
  }
  .welcome {
    position: absolute;
    right: 60px;
    bottom: 70px;
    margin: 0;
    font-family: "Roboto Condensed", sans-serif;
    font-style: italic;
    font-weight: 700;
    font-size: 48px;
    color: var(--white);
  }
</style>
</head>
<body>
  <section class="slide">
    <svg class="slide-art" width="1200" height="750" viewBox="0 0 1200 750" aria-hidden="false">
      <defs>
        <linearGradient id="photoTone" x1="0" y1="0" x2="1" y2="1">
          <stop offset="0" stop-color="var(--photo-light)" stop-opacity="0"/>
          <stop offset="0.35" stop-color="var(--photo-light)"/>
          <stop offset="1" stop-color="var(--photo-dark)"/>
        </linearGradient>
        <linearGradient id="bandTone" x1="0" y1="0" x2="1" y2="0">
          <stop offset="0" stop-color="var(--blue)" stop-opacity="0.85"/>
          <stop offset="1" stop-color="var(--navy-deep)" stop-opacity="0.95"/>
        </linearGradient>
      </defs>
      <rect class="photo-area" x="520" y="0" width="680" height="750" fill="url(#photoTone)"
            role="img" aria-label="Fotografia de um consultor de terno e gravata, braços cruzados"/>
      <path class="blue-band" d="M880 0 C800 230 740 500 660 750 L1200 750 L1200 0 Z" fill="url(#bandTone)"/>
      <path class="band-edge" d="M880 0 C800 230 740 500 660 750" fill="none" stroke="var(--blue-light)" stroke-width="10" opacity="0.8"/>
      <path class="band-edge-thin" d="M850 0 C772 230 712 500 632 750" fill="none" stroke="var(--blue-light)" stroke-width="3" opacity="0.5"/>
    </svg>

    <div class="brand">
      <div class="brand-square"></div>
      <div class="brand-name">Nórdica<br>Consultoria</div>
    </div>

    <p class="welcome">Seja bem vindo !</p>
  </section>
</body>
</html>
```